Harbor & Quillstone executive recruiting services

I started a plankfold website using an existing template and some of the original content is still on this UNpublished work in progress. I am an executive recruiter offering services to both Clients and Candidates in many sectors and using creative sourcing methodologies. I have 30+ years of business experience combined with my recruiting experience. I like the color teal and used it for the site I started. The tabs should be
About (me)
Services (for Clients and Candidates)
Industry Coverage
Recruiting Process (see attached flow chart)
Retained Agreement (see attached)
Personal Commitment
Testimonials
Content/articles/blogs etc
Contact
Updates

TO ALL DESIGNERS:
I have been granted a short extension to choose a design. Please resubmit designs using a new name DROVE EXECUTIVE SEARCH. Pls feel free to alert me with any questions and of course, when the edits are made.

thank you

Colette

Target Market(s)

Executives from Director, VP, SVP and C-Suite

Industry/Entity Type

recruiting industry for finance, Human Resoures, Sales/Marketing, Innovation/Transformation , Information Technology, Entertainment/Media/Telecommunications, Healthcare/Life Sciences,HCIT/Biotech

Font styles to use
Sans Serif

Colors
0094D4
00A9DD
6FCCEA
C7EBF8
E9F6FB

Requirements
Must have
• way to contact me - add calendar sign up
Nice to have
• process flow for the recruiting process (see attached)
Should not have
• guarantees

```html
<!DOCTYPE html>
<html lang="en">
<head>
<meta charset="utf-8">
<title>Harbor &amp; Quillstone Inc. — Executive Recruiting</title>
<link rel="stylesheet" href="https://fonts.googleapis.com/css2?family=Source+Sans+3:wght@400;600;700&family=Montserrat:wght@400;600;700;800&display=swap">
<style>
:root{
  --hero-deep:#1436f0;
  --hero-mid:#0a6cf5;
  --hero-cyan:#00d9ff;
  --accent:#1e86f3;
  --ink:#222831;
  --white:#ffffff;
  --band-left:#0c1f8a;
  --band-right:#0066b8;
  --field:#2b3f78;
  --footer-ink:#35237a;
}
*{box-sizing:border-box;margin:0;padding:0}
html,body{width:1200px;height:2260px;overflow:hidden;background:var(--white)}
body{position:relative;font-family:"Source Sans 3",sans-serif;color:var(--ink)}

/* Hero */
.hero{position:absolute;left:0;top:0;width:1200px;height:645px;overflow:hidden}
.hero-photo{position:absolute;inset:0;background:linear-gradient(100deg,var(--hero-deep) 0%,var(--hero-mid) 45%,var(--hero-cyan) 100%)}
.nav-link{position:absolute;color:var(--white);font-size:13.5px;font-weight:600;letter-spacing:.2px;white-space:nowrap;transform:translate(-50%,-50%)}
.utility-nav{position:absolute;right:150px;top:22px;display:flex;gap:22px}
.utility-nav span{color:var(--white);opacity:.78;font-size:13.5px;font-weight:600}
.brand-badge{position:absolute;left:493px;top:24px;width:176px;height:176px;border-radius:50%;background:var(--white);border:3px solid #d9dde6;display:flex;align-items:center;justify-content:center;text-align:center}
.brand-badge span{font-size:19px;font-weight:600;color:#111;line-height:1.15}
.hero-title{position:absolute;left:0;width:1160px;top:244px;text-align:center;color:var(--white);font-size:53px;font-weight:400;letter-spacing:-.5px;line-height:64px}
.hero-sub{position:absolute;left:0;width:1160px;top:302px;text-align:center;color:var(--white);font-size:27px;font-weight:400;line-height:34px}
.hero-intro{position:absolute;left:362px;top:357px;width:430px;color:var(--white);font-size:11.2px;font-weight:600;line-height:19.5px}
.btn{position:absolute;top:460px;width:198px;height:44px;border-radius:22px;display:flex;align-items:center;justify-content:center;font-size:13px;letter-spacing:.5px}
.btn-clients{left:361px;background:var(--white);color:#333}
.btn-candidates{left:589px;border:2px solid var(--white);color:var(--white)}

/* Process */
.process-title{position:absolute;left:0;width:1200px;top:690px;text-align:center;font-size:45px;line-height:55px;font-weight:400;color:var(--ink)}
.process-art{position:absolute;left:0;top:850px}
.step{position:absolute;font-family:"Montserrat",sans-serif;font-weight:700;font-size:12.5px;letter-spacing:1.4px;line-height:16px;color:var(--ink);white-space:nowrap}
.step .num{color:var(--accent);margin-right:4px}
.step .cont{padding-left:16px;display:block}

.book-call{position:absolute;left:612px;top:1548px;width:541px;height:43px;border-radius:22px;background:var(--accent);color:var(--white);font-family:"Montserrat",sans-serif;font-size:13px;font-weight:600;display:flex;align-items:center;justify-content:center;z-index:2}

/* Discuss band */
.discuss{position:absolute;left:0;top:1569px;width:1200px;height:370px;background:linear-gradient(105deg,var(--band-left) 0%,var(--band-right) 100%)}
.discuss h2{position:absolute;left:0;width:1194px;top:63px;text-align:center;color:var(--white);font-family:"Montserrat",sans-serif;font-weight:800;font-size:36px}
.discuss p{position:absolute;left:0;width:1194px;top:128px;text-align:center;color:#e4ecff;font-family:"Montserrat",sans-serif;font-size:13px;letter-spacing:1.2px;line-height:16px}
.email-field{position:absolute;left:362px;top:232px;width:340px;height:41px;background:var(--field);border-radius:4px 0 0 4px;color:#c9d2ea;font-family:"Montserrat",sans-serif;font-size:12px;letter-spacing:1px;padding:0 14px;display:flex;align-items:center;gap:9px}
.schedule-btn{position:absolute;left:686px;top:232px;width:143px;height:41px;border-radius:21px;background:var(--white);color:#222;font-family:"Montserrat",sans-serif;font-size:10px;font-weight:700;letter-spacing:1.2px;display:flex;align-items:center;justify-content:center;box-shadow:0 4px 10px rgba(0,0,0,.2)}

/* Footer */
.footer-badge{position:absolute;left:557px;top:1981px;width:94px;height:94px;border-radius:50%;border:1.5px solid #333;display:flex;align-items:center;justify-content:center;text-align:center}
.footer-badge span{font-size:11px;font-weight:600;color:#111;line-height:1.15}
.footer-name{position:absolute;left:0;width:1196px;top:2101px;text-align:center;color:var(--footer-ink);font-size:23px}
.footer-tag{position:absolute;left:0;width:1200px;top:2144px;text-align:center;color:var(--footer-ink);font-size:17px;font-weight:700}
.legal{position:absolute;left:0;width:1200px;top:2198px;text-align:center;font-size:11px;line-height:19px;color:#222}
</style>
</head>
<body>

<header class="hero">
  <div class="hero-photo" role="img" aria-label="Photo of two smiling colleagues at a laptop, tinted in blue and cyan"></div>
  <nav class="utility-nav">
    <span>Articles</span><span>Updates</span><span>Contact</span>
  </nav>
  <nav>
    <span class="nav-link" style="left:150px;top:112px">About</span>
    <span class="nav-link" style="left:218px;top:112px">Services</span>
    <span class="nav-link" style="left:308px;top:112px">Industry Coverage</span>
    <span class="nav-link" style="left:432px;top:112px">Recruiting Process</span>
    <span class="nav-link" style="left:745px;top:112px">Retained Agreement</span>
    <span class="nav-link" style="left:887px;top:112px">Personal Commitment</span>
    <span class="nav-link" style="left:1010px;top:112px">Testimonials</span>
  </nav>
  <div class="brand-badge"><span>Harbor &amp;<br>Quillstone</span></div>
  <h1 class="hero-title">HARBOR &amp; QUILLSTONE INC.</h1>
  <p class="hero-sub">30+ years Experience in Hiring</p>
  <p class="hero-intro">Welcome to the Harbor &amp; Quillstone recruiting website! If you are looking to grow your team or change careers, you’re at the right place. I’m Colette Drove, the Founder and President of H&amp;Q, dedicated to matching job openings with job seekers.</p>
  <a class="btn btn-clients">FOR CLIENTS</a>
  <a class="btn btn-candidates">FOR CANDIDATES</a>
</header>

<section class="process">
  <h2 class="process-title">Confessions of<br>Recruiting strategy</h2>
  <svg class="process-art" width="1200" height="600" viewBox="0 850 1200 600" aria-hidden="true">
    <g fill="none" stroke="#1e86f3" stroke-linecap="round">
      <path d="M-10 946 C200 950 420 960 600 990 C760 1015 900 1050 987 1113" stroke-width="15"/>
      <path d="M987 1113 C1040 1160 1030 1210 960 1245" stroke-width="18"/>
      <path d="M960 1245 C830 1320 600 1365 380 1380 C200 1390 80 1388 -10 1392" stroke-width="28"/>
    </g>
    <g fill="#1e86f3" stroke="#ffffff" stroke-width="4">
      <circle cx="59" cy="948" r="18"/>
      <circle cx="272" cy="956" r="18"/>
      <circle cx="495" cy="974" r="18"/>
      <circle cx="696" cy="1005" r="18"/>
      <circle cx="873" cy="1052" r="18"/>
      <circle cx="987" cy="1113" r="19"/>
      <circle cx="932" cy="1263" r="25"/>
      <circle cx="748" cy="1322" r="31"/>
      <circle cx="546" cy="1360" r="32"/>
      <circle cx="306" cy="1383" r="37"/>
      <circle cx="58" cy="1383" r="47"/>
    </g>
  </svg>
  <div class="step" style="left:57px;top:878px"><span class="num">1.</span>CLIENT CONSULT &amp;<span class="cont">ADVEISEMENT</span></div>
  <div class="step" style="left:266px;top:893px"><span class="num">2.</span>SOURCING</div>
  <div class="step" style="left:491px;top:915px"><span class="num">3.</span>CONDIDATE LIST<span class="cont">GENERATION</span></div>
  <div class="step" style="left:687px;top:949px"><span class="num">4.</span>INTERNAL TEAM<span class="cont">REVIEW</span></div>
  <div class="step" style="left:868px;top:984px"><span class="num">5.</span>CONDIDATE OUTREACH,<span class="cont">PRE. QUALIFYING INTERVIEWS &amp;</span><span class="cont">DOCUEMNTATION</span></div>
  <div class="step" style="left:980px;top:1062px"><span class="num">6.</span>INTERNAL ASSASEMENT,<span class="cont">PRESENT CONDIDATES</span></div>
  <div class="step" style="left:937px;top:1316px"><span class="num">7.</span>CONDIDATE<span class="cont">RESPONSE REVIEWS</span></div>
  <div class="step" style="left:748px;top:1384px"><span class="num">8.</span>INTERVIEW&nbsp; MANAGEMENT</div>
  <div class="step" style="left:544px;top:1421px"><span class="num">9.</span>INTERVIEW PREP</div>
  <div class="step" style="left:303px;top:1452px"><span class="num">10.</span>POST INTERVIEW<span class="cont">&nbsp;FEEDBACK</span></div>
  <div class="step" style="left:51px;top:1466px"><span class="num">11.</span>OFFER PRESENTATION</div>
  <a class="book-call">Book a Consultation</a>
</section>

<section class="discuss">
  <h2>Let’s discuss</h2>
  <p>how we can work together to find the ideal fit for<br>your company or for you, as a candidate.</p>
  <div class="email-field">
    <svg width="14" height="14" viewBox="0 0 14 14" aria-hidden="true"><rect x="1" y="2.5" width="12" height="10.5" rx="1.5" fill="none" stroke="#c9d2ea" stroke-width="1.3"/><path d="M1 6h12M4.5 1v3M9.5 1v3" stroke="#c9d2ea" stroke-width="1.3"/></svg>
    Your email
  </div>
  <a class="schedule-btn">BOOK A CALL</a>
</section>

<footer>
  <div class="footer-badge"><span>Harbor &amp;<br>Quillstone</span></div>
  <p class="footer-name">HARBOR &amp; QUILLSTONE, INC.</p>
  <p class="footer-tag">30+ Years in Hiring</p>
  <p class="legal">Copyright © 2022. Use of this website constitutes acceptance of our User Agreement and Privacy Policy.<br>*Conditions apply please see our money back refund policy.</p>
</footer>

</body>
</html>
```